Informational Website for SOLVANE-SOciety of Linked VAriable NEtwork Health Analysts

I need an informational website to help establish us as a legitimate entity. This will help us as we seek funding in to perform the research we intend to carry out. We are a newly formed group of family physicians and primary care researchers from 9 different countries around the world. We have access to electronic medical record data and/or health insurance claims data in our respective countries. We intend to perform international comparative studies in primary care. Our set of projects are to study the impact of the COVID-19 pandemic on primary care in our respective countries and around the world.
I've already purchased a domain and website from Plonko. It is a premium account. The domain is https://www.solvanehealthnet.org

Target Market(s)

Researchers, policy makers, universities, research funding agencies

Coding

Coded - Design and coding required

Number of Pages Required

5+ page

Font styles to use
Sans Serif

Requirements
Must have
• Must have our logo and an interactive map of the world highlighting Canada, Australia, China (including Hong Kong), Norway, Singapore, South Korea, Sweden, United Kingdom, United States.
This map must be editable such that we can add or remove countries and cities as we evolve. Please see attached brief.
Nice to have
• Nice to depict primary care and big data research

```html
<!DOCTYPE html>
<html lang="en">
<head>
<meta charset="utf-8">
<title>SOLVANE — Society of Linked Variable Network Health Analysts</title>
<link href="https://fonts.googleapis.com/css2?family=Montserrat:wght@500;600;700;800&family=Open+Sans:wght@400;600;700&display=swap" rel="stylesheet">
<style>
:root{
  --navy:#10306e;
  --navy-deep:#0b2458;
  --green:#7cb518;
  --green-dark:#6a9e10;
  --ice:#e8eff9;
  --ink:#2b2f3a;
  --muted:#6b7280;
  --white:#ffffff;
  --line:#d9dee8;
}
*{box-sizing:border-box;margin:0;padding:0}
html,body{width:1200px;height:3636px;overflow:hidden}
body{font-family:"Open Sans",Arial,sans-serif;color:var(--ink);background:var(--white);position:relative}
h1,h2,h3,.btn,.nav a{font-family:"Montserrat",Arial,sans-serif}
.btn{display:inline-flex;align-items:center;gap:10px;background:var(--green);color:var(--white);font-size:13px;font-weight:700;letter-spacing:.5px;padding:12px 26px;border-radius:24px;text-transform:uppercase}
.btn .dot{width:18px;height:18px;border-radius:50%;background:var(--white);display:inline-flex;align-items:center;justify-content:center}
.section-title{text-align:center;font-size:38px;font-weight:700;letter-spacing:1px;color:var(--navy)}
.section-title span{color:var(--green)}

/* header */
.site-header{position:absolute;top:0;left:0;width:1200px;height:80px;background:var(--white);z-index:3;box-shadow:0 2px 8px rgba(0,0,0,.08)}
.brand{position:absolute;left:104px;top:-14px;width:136px;height:136px;border-radius:50%;background:var(--white);display:flex;align-items:center;justify-content:center;box-shadow:0 4px 12px rgba(0,0,0,.15)}
.brand span{font-family:"Montserrat",sans-serif;font-weight:800;font-size:22px;color:var(--navy);letter-spacing:.5px}
.nav{position:absolute;left:378px;top:0;height:80px;display:flex;align-items:center;gap:34px}
.nav a{font-size:15px;font-weight:600;color:var(--ink);text-decoration:none;position:relative}
.nav a.active{color:var(--green)}
.nav a.active::after{content:"";position:absolute;left:0;right:0;bottom:-10px;height:2px;background:var(--green)}
.header-icons{position:absolute;left:1000px;top:28px;display:flex;gap:18px}

/* hero */
.hero{position:absolute;top:80px;left:0;width:1200px;height:680px;background:linear-gradient(100deg,#0d2c5a 0%,#1d5d95 45%,#4fa0d3 70%,#a9bfd3 100%)}
.hero-copy{position:absolute;left:108px;top:262px;color:var(--white)}
.hero-copy h1{font-size:40px;font-weight:800;letter-spacing:1px}
.hero-copy p{font-size:17px;line-height:24px;width:390px;margin:10px 0 26px}

/* research */
.research{position:absolute;top:760px;left:0;width:1200px;height:580px}
.research .section-title{margin-top:84px}
.cards{position:absolute;top:180px;left:108px;display:flex;gap:20px}
.card{width:313px;height:340px;background:var(--navy);border-radius:60px 6px 60px 6px;color:var(--white);text-align:center;padding:30px 26px 0;position:relative}
.card.featured{background:var(--green)}
.card .icon{width:78px;height:78px;margin:0 auto 20px;border-radius:50%;border:2px solid rgba(255,255,255,.7);display:flex;align-items:center;justify-content:center}
.card h3{font-size:17px;font-weight:700;margin-bottom:12px}
.card p{font-size:13px;line-height:19px}
.card .more{position:absolute;right:30px;bottom:26px;display:flex;align-items:center;gap:8px;font-family:"Montserrat",sans-serif;font-size:12px;font-weight:700}
.card .more .dot{width:18px;height:18px;border-radius:50%;background:var(--white)}

/* about */
.about{position:absolute;top:1360px;left:0;width:1200px;height:470px;background:var(--ice)}
.about-copy{position:absolute;left:108px;top:86px;width:530px}
.about-copy h2{font-size:36px;font-weight:700;color:var(--navy)}
.about-copy h2 span{color:var(--green)}
.about-copy p{font-size:13px;line-height:21px;color:var(--muted);margin-top:16px}
.about-copy .btn{margin-top:24px}
.about-visual{position:absolute;left:660px;top:100px;width:440px;height:250px;border-radius:14px;background:radial-gradient(circle at 40% 50%,#b8cbe6 0%,#dfe8f5 70%)}

/* news */
.news{position:absolute;top:1830px;left:0;width:1200px;height:670px}
.news .section-title{margin-top:120px}
.news-grid{position:absolute;top:190px;left:108px;display:flex;gap:20px}
.news-card{width:230px;height:340px;background:var(--white);box-shadow:0 3px 12px rgba(0,0,0,.1)}
.news-card .photo{height:190px}
.news-card .meta{display:flex;align-items:center;gap:8px;font-size:11px;color:var(--muted);padding:14px 16px 6px}
.news-card p{font-size:13px;line-height:19px;padding:0 16px;color:var(--ink)}
.news .btn{position:absolute;left:536px;top:572px;padding:10px 24px}

/* contact */
.contact{position:absolute;top:2500px;left:0;width:1200px;height:1136px;background:linear-gradient(180deg,#163a7c 0%,#0f2d66 100%);color:var(--white)}
.world-map{position:absolute;left:200px;top:40px;width:800px;height:470px;border-radius:20px;background:radial-gradient(ellipse at 50% 50%,#7d97c4 0%,#3d5f9c 60%,rgba(22,58,124,0) 100%)}
.contact h2{position:absolute;top:590px;width:1200px;text-align:center;font-size:38px;font-weight:700}
.contact-info{position:absolute;top:660px;left:170px;display:flex;gap:70px}
.info-item{display:flex;gap:14px;width:260px;font-size:13px;line-height:19px}
.info-item .ic{flex:none;width:40px;height:40px;border-radius:50%;background:var(--green);display:flex;align-items:center;justify-content:center}
.form{position:absolute;top:734px;left:338px;width:524px}
.row{display:flex;gap:12px;margin-bottom:12px}
.field{flex:1;height:40px;background:var(--white);border:1px solid var(--line);font-size:12px;color:#8a8f99;padding:12px 14px}
.field.msg{height:130px}
.form .btn{display:flex;width:140px;justify-content:center;margin:22px auto 0;padding:11px 0}
.copyright{position:absolute;top:1094px;width:1200px;text-align:center;font-size:12px;color:#d2dbeb}
</style>
</head>
<body>

<header class="site-header">
  <div class="brand"><span>SOLVANE</span></div>
  <nav class="nav">
    <a class="active">Home</a><a>About Us</a><a>What We Do</a><a>Our Institutions</a><a>Blog</a><a>Contact Us</a>
  </nav>
  <div class="header-icons">
    <svg width="20" height="20" viewBox="0 0 20 20"><path d="M10 2a5 5 0 0 0-5 5v4l-2 3h14l-2-3V7a5 5 0 0 0-5-5zM8 16a2 2 0 0 0 4 0" fill="none" stroke="#2b2f3a" stroke-width="1.6"/></svg>
    <svg width="20" height="20" viewBox="0 0 20 20"><circle cx="10" cy="10" r="9" fill="#2b2f3a"/><circle cx="10" cy="8" r="3" fill="#fff"/><path d="M4.5 15.5a6.5 5 0 0 1 11 0" fill="#fff"/></svg>
    <svg width="10" height="20" viewBox="0 0 10 20"><path d="M2 8l3 3 3-3" fill="none" stroke="#2b2f3a" stroke-width="1.6"/></svg>
  </div>
</header>

<section class="hero" role="img" aria-label="Doctor holding a tablet with floating medical data icons">
  <div class="hero-copy">
    <h1>SOLVANE</h1>
    <p>We are family physicians and primary care researchers from nine different countries.</p>
    <span class="btn">Get Started</span>
  </div>
</section>

<section class="research">
  <h2 class="section-title">OUR <span>RESEARCH</span></h2>
  <div class="cards">
    <article class="card">
      <div class="icon"><svg width="34" height="34" viewBox="0 0 34 34"><rect x="7" y="4" width="20" height="26" rx="2" fill="none" stroke="#fff" stroke-width="2"/><path d="M11 11h12M11 16h12M11 21h8" stroke="#fff" stroke-width="2"/></svg></div>
      <h3>PUBLICATIONS</h3>
      <p>Lorem ipsum dolor sit amet, consectetur adipiscing elit, sed eiusmod tempor incididunt ut labore dolore magna aliqua.</p>
      <span class="more">READ MORE <span class="dot"></span></span>
    </article>
    <article class="card featured">
      <div class="icon"><svg width="34" height="34" viewBox="0 0 34 34"><rect x="4" y="5" width="26" height="17" fill="none" stroke="#fff" stroke-width="2"/><path d="M17 22v7M11 30h12M9 17l6-5 4 3 6-6" fill="none" stroke="#fff" stroke-width="2"/></svg></div>
      <h3>PRESENTATIONS</h3>
      <p>Lorem ipsum dolor sit amet, consectetur adipiscing elit, sed eiusmod tempor incididunt ut labore dolore magna aliqua.</p>
      <span class="more">READ MORE <span class="dot"></span></span>
    </article>
    <article class="card">
      <div class="icon"><svg width="34" height="34" viewBox="0 0 34 34"><circle cx="17" cy="17" r="12" fill="none" stroke="#fff" stroke-width="2"/><path d="M21 12h-5a2.5 2.5 0 0 0 0 5h2a2.5 2.5 0 0 1 0 5h-5M17 9v16" fill="none" stroke="#fff" stroke-width="2"/></svg></div>
      <h3>FUNDING</h3>
      <p>Lorem ipsum dolor sit amet, consectetur adipiscing elit, sed eiusmod tempor incididunt ut labore dolore magna aliqua.</p>
      <span class="more">READ MORE <span class="dot"></span></span>
    </article>
  </div>
</section>

<section class="about">
  <div class="about-copy">
    <h2>ABOUT <span>US</span></h2>
    <p>Lorem ipsum dolor sit amet, consectetur adipiscing elit, sed do eiusmod tempor incididunt ut labore et dolore magna aliqua. Ut enim ad minim veniam, quis nostrud exercitation ullamco laboris nisi ut aliquip ex commodo consequat. Duis aute irure dolor in reprehenderit in voluptate velit esse cillum dolore eu fugiat nulla pariatur. Excepteur sint occaecat.</p>
    <p>Lorem ipsum dolor sit amet, consectetur adipiscing elit, sed do eiusmod tempor incididunt ut labore et dolore magna.</p>
    <span class="btn">Read More <span class="dot"></span></span>
  </div>
  <div class="about-visual" role="img" aria-label="Illustration of a globe with a stethoscope"></div>
</section>

<section class="news">
  <h2 class="section-title">SOLVANE <span>NEWS</span></h2>
  <div class="news-grid">
    <article class="news-card"><div class="photo" role="img" aria-label="Tablet showing health data charts" style="background:linear-gradient(135deg,#9fb9d4,#4b6f96)"></div><div class="meta">▣ 01 Dec 2020</div><p>Maecenas vel accumsan quam varius imperdiet vel eget</p></article>
    <article class="news-card"><div class="photo" role="img" aria-label="Physician with digital medical icons" style="background:linear-gradient(135deg,#d6e3ef,#7fa6c8)"></div><div class="meta">▣ 01 Dec 2020</div><p>Vivamus efficitur ex orci elementum, malesuada orci eget, feugiat</p></article>
    <article class="news-card"><div class="photo" role="img" aria-label="Researchers working in a bright office" style="background:linear-gradient(135deg,#8fb2d6,#2f5f93)"></div><div class="meta">▣ 01 Dec 2020</div><p>Etiam mattis augue odio posuere amet tempus leo fames</p></article>
    <article class="news-card"><div class="photo" role="img" aria-label="Laboratory equipment in blue light" style="background:linear-gradient(135deg,#bcd3ea,#3b78b3)"></div><div class="meta">▣ 01 Dec 2020</div><p>Etiam vel massa bibendum tellus venenatis feugiat massa</p></article>
  </div>
  <span class="btn">View All <span class="dot"></span></span>
</section>

<section class="contact">
  <div class="world-map" role="img" aria-label="World map highlighting member countries with location pins"></div>
  <h2>CONTACT US</h2>
  <div class="contact-info">
    <div class="info-item"><span class="ic"><svg width="18" height="18" viewBox="0 0 18 18"><path d="M9 1a6 6 0 0 0-6 6c0 4.5 6 10 6 10s6-5.5 6-10a6 6 0 0 0-6-6z" fill="#fff"/><circle cx="9" cy="7" r="2.2" fill="#7cb518"/></svg></span><span>123, Lorem ipsum dolor sit<br>amet, consectetur</span></div>
    <div class="info-item"><span class="ic"><svg width="18" height="18" viewBox="0 0 18 18"><rect x="2" y="4" width="14" height="10" fill="#fff"/><path d="M2 4l7 6 7-6" fill="none" stroke="#7cb518" stroke-width="1.4"/></svg></span><span>Mail us :<br>info@solvanemail.org</span></div>
    <div class="info-item"><span class="ic"><svg width="18" height="18" viewBox="0 0 18 18"><path d="M4 2l3 3-1.5 2.5a9 9 0 0 0 5 5L13 11l3 3-2 2C8 16 2 10 2 4z" fill="#fff"/></svg></span><span>Call us :<br>+1 555 014 2207</span></div>
  </div>
  <div class="form">
    <div class="row"><div class="field">Enter Your Name</div><div class="field">Enter Your Email</div></div>
    <div class="row"><div class="field">Enter Your Subject</div></div>
    <div class="row"><div class="field msg">Type your Message here</div></div>
    <span class="btn">Submit</span>
  </div>
  <p class="copyright">© Copyrights 2020 SOLVANE. All Rights Reserved</p>
</section>

</body>
</html>
```